Brochure Design Project

This will be a tri-fold full 8.5x11 brochure that will be distributed and sitting in Oncology offices all throughout the US. It is a lead generation and referral designed piece that it to target all patients, Cancer primarily, but all critically ill patients and seniors above the age of 70. We want our service to go beyond just a financial transaction, we want to educate patients of their rights within a life insurance policy and if we cannot help them personally, do want to assist them by referring them to other agencies and non profits than can. ( I want to redesign the brochure attached, it can be very similar and need only minor changes to content, but would welcome all suggestions on improving message, and in gaining attention, picture substitutions and change of colors, along with the layout itself can be improved upon, and I need this piece to look very professional and appropriate for medical offices. I will be needing assistance on several upcoming projects and will also have great printing demands.

Target Market(s)

Cancer patients
all chronically and critically ill patients
all seniors above age 70

Industry/Entity Type

Life Insurance

Requirements
Must have
• Cancer and the terminally ill
Nice to have
• seniors above 70

```html
<!DOCTYPE html>
<html lang="en">
<head>
<meta charset="utf-8">
<title>Beacon Settlements Tri-fold Brochure</title>
<link rel="stylesheet" href="https://fonts.googleapis.com/css2?family=PT+Sans:wght@400;700&family=Roboto+Condensed:wght@400;700&display=swap">
<style>
  :root {
    --canvas: #e6e4e4;
    --paper: #ffffff;
    --brand-blue: #4a78bd;
    --brand-orange: #f6a81c;
    --ink: #111111;
    --dot-brown: #6b4a2f;
    --photo-warm: #c9b3a6;
    --photo-warm-dark: #5a4a44;
    --photo-cool: #e9dfd6;
    --photo-cool-dark: #b8a9a6;
  }
  * { box-sizing: border-box; margin: 0; padding: 0; }
  html, body { width: 1200px; height: 900px; overflow: hidden; background: var(--canvas); }
  .brochure { position: relative; width: 1200px; height: 900px; font-family: "PT Sans", Arial, sans-serif; color: var(--ink); }
  .panel { position: absolute; top: 14px; height: 870px; background: var(--paper); }

  /* Left panel: reply mail */
  .panel--reply { left: 28px; width: 362px; }
  .reply-banner {
    position: absolute; left: 4px; top: 0; width: 362px; height: 204px;
    background: var(--brand-blue); color: var(--paper);
    display: flex; align-items: center; justify-content: center; text-align: center;
    font-weight: 700; font-size: 44px; line-height: 1.25; letter-spacing: 0.5px;
  }
  .brand-name {
    position: absolute; left: 0; width: 100%; text-align: center;
    color: var(--brand-blue); font-weight: 700; font-family: "PT Sans", Arial, sans-serif;
  }
  .panel--reply .brand-name { top: 270px; font-size: 30px; line-height: 1.1; }
  .reply-box {
    position: absolute; left: 30px; top: 396px; width: 310px; height: 310px;
    border: 4px dotted var(--dot-brown); border-radius: 14px; text-align: center;
  }
  .reply-box__intro { margin-top: 24px; font-size: 18px; line-height: 1.35; }
  .reply-box__phone { margin-top: 60px; font-size: 45px; font-weight: 700; letter-spacing: -0.5px; }
  .reply-box__note { margin-top: 64px; font-size: 16px; line-height: 1.35; }
  .reply-address { position: absolute; left: 0; top: 780px; width: 100%; text-align: center; }
  .reply-address__name { font-size: 25px; font-weight: 700; }
  .reply-address__line { font-size: 18px; line-height: 1.35; }

  /* Middle panel: benefits */
  .panel--benefits { left: 418px; width: 363px; background: var(--brand-orange); font-family: "Roboto Condensed", "Arial Narrow", sans-serif; color: var(--paper); }
  .photo { position: absolute; display: block; }
  .photo--portrait { left: 0; top: 0; width: 363px; height: 374px;
    background: linear-gradient(160deg, var(--photo-warm) 0%, var(--photo-warm-dark) 100%); }
  .benefits__title { position: absolute; left: 24px; top: 384px; font-size: 24px; }
  .benefits__list { position: absolute; left: 34px; top: 447px; list-style: none; font-size: 16px; line-height: 21.3px; }
  .benefits__more { position: absolute; left: 34px; top: 664px; font-size: 23px; }
  .benefits__cta { position: absolute; left: 0; top: 772px; width: 100%; text-align: center; }
  .benefits__cta-line { font-size: 24px; }
  .benefits__cta-phone { font-size: 47px; font-weight: 700; line-height: 1.05; letter-spacing: 0.5px; }

  /* Right panel: cover */
  .panel--cover { left: 805px; width: 361px; }
  .panel--cover .brand-name { top: 118px; font-size: 34px; line-height: 1.1; }
  .photo--bedside { left: 0; top: 274px; width: 361px; height: 367px;
    background: linear-gradient(120deg, var(--photo-cool) 0%, var(--photo-cool-dark) 100%); }
  .cover-banner {
    position: absolute; left: 0; top: 666px; width: 361px; height: 204px;
    background: var(--brand-blue); color: var(--paper); text-align: center;
    font-family: "Roboto Condensed", "Arial Narrow", sans-serif;
  }
  .cover-banner__title { margin-top: 26px; font-size: 28px; }
  .cover-banner__sub { margin-top: 20px; font-size: 24px; }
</style>
</head>
<body>
<main class="brochure">
  <section class="panel panel--reply">
    <div class="reply-banner">BUSINESS<br>REPLY MAIL</div>
    <div class="brand-name">Beacon<br>Settlements</div>
    <div class="reply-box">
      <p class="reply-box__intro">Please return the attached postcard<br>or call TOLL FREE</p>
      <p class="reply-box__phone">800-555-0148</p>
      <p class="reply-box__note">All Communication will be kept<br>strictly confidential</p>
    </div>
    <address class="reply-address" style="font-style:normal">
      <p class="reply-address__name">Beacon Settlements</p>
      <p class="reply-address__line">480, Willow Creek, Dr. Marysville,<br>Ohio - 43040</p>
    </address>
  </section>

  <section class="panel panel--benefits">
    <div class="photo photo--portrait" role="img" aria-label="Photo of a young woman in a pink headscarf resting her head on her knee"></div>
    <h2 class="benefits__title" style="font-weight:400">Hope is Our Desired Gift to You</h2>
    <ul class="benefits__list">
      <li>Reduce Financial Stress</li>
      <li>Pay for uninsured Healthcare cost</li>
      <li>Pay for alternative treatment</li>
      <li>Improve quality of Life</li>
      <li>Pay off Debt</li>
      <li>Take a long awaited&nbsp; vacation or Dream trip</li>
      <li>Make cash gifts to family and friends</li>
      <li>Fulfill life wishes</li>
      <li>Pay for College Funding</li>
      <li>Make Home Improvements</li>
    </ul>
    <p class="benefits__more">and many more...</p>
    <div class="benefits__cta">
      <p class="benefits__cta-line">We are Waiting to Help</p>
      <p class="benefits__cta-phone">800-555-0148</p>
    </div>
  </section>

  <section class="panel panel--cover">
    <div class="brand-name">Beacon<br>Settlements</div>
    <div class="photo photo--bedside" role="img" aria-label="Photo of a patient resting in bed with an oxygen tube"></div>
    <div class="cover-banner">
      <p class="cover-banner__title">Discover Financial Freedom</p>
      <p class="cover-banner__sub">We are Waiting to Help</p>
    </div>
  </section>
</main>
</body>
</html>
```